Business Card Design Project

This is the first time we use our new logo. We need a business card that we can use both on our institutional corporate relationships and also that works for our staff that deals with consumers directly.

VELUNDA is a new company dedicated to empower consumers and to provide them with the best choices for specialized health care using the latest telemedicine technology (medicine at a distance via videoconference).

We want to print this cards in high quality materials and process. We will like designs that allow us to use UV spot varnish and other techniques that will differentiate us.

We are including Two different versions of Color logos. In addition we are including white over black background logos. Those can be used replacing the black for a color.

Please note this is the first time we will be creating any corporate materials with our new logo and colors.

Target Market(s)

34+ consumers of medium high and high socioeconomic levels.

Industry/Entity Type

Health

Requirements
Must have
• Our logo on its original colors
Should not have
• Any other graphical element or design that is not our logo

```html
<!DOCTYPE html>
<html lang="en">
<head>
<meta charset="utf-8">
<title>VELUNDA Business Card</title>
<link rel="stylesheet" href="https://fonts.googleapis.com/css2?family=Jost:wght@400;500;600&display=swap">
<style>
  :root {
    --page-bg: #e6e7e9;
    --card-face: #f1f3f5;
    --card-face-edge: #dfe3e8;
    --brand-navy: #1b4a78;
    --brand-blue: #1f67ab;
    --brand-blue-deep: #175a98;
    --ink: #1d4a7c;
  }
  * { margin: 0; padding: 0; box-sizing: border-box; }
  html, body {
    width: 1200px;
    height: 880px;
    overflow: hidden;
    background: var(--page-bg);
    font-family: "Jost", "Futura", sans-serif;
  }
  .sheet {
    position: relative;
    width: 1200px;
    height: 880px;
    display: flex;
    align-items: center;
    justify-content: center;
    gap: 40px;
  }
  .card {
    position: relative;
    width: 560px;
    height: 320px;
    overflow: hidden;
    box-shadow: 0 6px 18px rgba(0,0,0,0.18);
  }

  /* Front */
  .card-front {
    background: linear-gradient(135deg, var(--card-face) 0%, var(--card-face-edge) 100%);
  }
  .front-band {
    position: absolute;
    left: 0; bottom: 0;
    width: 560px; height: 60px;
  }
  .brand-block {
    position: absolute;
    left: 40px; top: 88px;
    width: 200px;
    display: flex;
    flex-direction: column;
    align-items: center;
    gap: 22px;
  }
  .brand-dot {
    width: 58px; height: 58px;
    border-radius: 50%;
    background: var(--brand-blue);
  }
  .brand-name {
    font-weight: 600;
    font-size: 40px;
    letter-spacing: 3px;
    color: var(--brand-navy);
  }
  .divider {
    position: absolute;
    left: 262px; top: 44px;
    width: 2px; height: 186px;
    background: var(--brand-navy);
  }
  .contact {
    position: absolute;
    left: 290px; top: 44px;
    color: var(--ink);
  }
  .contact-name {
    font-weight: 600;
    font-size: 22px;
    line-height: 1.1;
  }
  .contact-role {
    font-size: 12px;
    margin-bottom: 18px;
  }
  .contact-lines {
    font-size: 14px;
    line-height: 1.4;
    margin-bottom: 12px;
  }
  .contact-address {
    font-size: 14px;
    line-height: 1.45;
  }

  /* Back */
  .card-back {
    background: linear-gradient(160deg, var(--brand-blue) 0%, var(--brand-blue-deep) 100%);
  }
</style>
</head>
<body>
  <main class="sheet">
    <section class="card card-front" aria-label="Business card front">
      <div class="brand-block">
        <span class="brand-dot"></span>
        <span class="brand-name">VELUNDA</span>
      </div>
      <div class="divider"></div>
      <div class="contact">
        <p class="contact-name">Name Surname</p>
        <p class="contact-role">manager</p>
        <p class="contact-lines">555.204.1386<br>dmarlo@brisvantcare.com<br>www.brisvantcare.com</p>
        <p class="contact-address">Your Address Goes Here<br>Another Row<br>City, State, Zipcode</p>
      </div>
      <svg class="front-band" viewBox="0 0 560 60" preserveAspectRatio="none" aria-hidden="true">
        <path d="M0 28 Q280 48 560 40 L560 60 L0 60 Z" fill="var(--brand-blue)"/>
      </svg>
    </section>

    <section class="card card-back" aria-label="Business card back"></section>
  </main>
</body>
</html>
```